Webdesign für Arztpraxis
Zielgruppe
Arztpraxis für Dermatologie am Lindenhof.
Lindenhof ist ein Spital/Krankenhaus hier in Basel, Schweiz.
Kunden sind in jeder Altersstufe für Hauterkrankungen.
Behandlung Chirugisch, konservativ und mit Laser.
Aufgabenstellung
Brandguide und Logo anbei
Farben: #395722 und #ABCF8A
Beispielseite, die gefällt: https://hautpraxis-brunner-kessler.example

```html
<!DOCTYPE html>
<html lang="de">
<head>
<meta charset="utf-8">
<title>Dermatologie am Lindenhof</title>
<link href="https://fonts.googleapis.com/css2?family=Montserrat:wght@400;500;600;700&display=swap" rel="stylesheet">
<style>
:root{
  --green:#395722;
  --light:#ABCF8A;
  --paper:#f6f6f6;
  --white:#ffffff;
  --text:#555555;
}
*{margin:0;padding:0;box-sizing:border-box}
html,body{width:1200px;height:4338px;overflow:hidden}
body{font-family:'Montserrat',sans-serif;background:var(--white);position:relative;color:var(--green)}
.abs{position:absolute}
section,header,footer{position:absolute;left:0;width:1200px;overflow:hidden}
.brand{font-family:'Montserrat',sans-serif;font-weight:500;color:var(--green);line-height:1.05}
.brand .big{font-size:20px;display:block}
.brand .small{font-size:12px;display:block;padding-left:2px}
.brand .dot{position:absolute;left:-26px;top:6px;width:16px;height:16px;border-radius:50%;background:var(--light)}
/* header */
.site-header{top:0;height:118px;background:var(--white)}
.nav a{position:absolute;top:50px;font-size:12px;letter-spacing:2px;color:var(--green);text-decoration:none;font-weight:500}
.nav a.active{border-bottom:1px solid var(--green);padding-bottom:6px}
/* hero */
.hero{top:118px;height:682px;background:var(--green)}
.hero h1{left:32px;top:72px;font-size:46px;line-height:56px;font-weight:700;color:var(--white);letter-spacing:2px;z-index:3}
.hero .lead{left:32px;top:232px;font-size:22px;line-height:26px;font-weight:700;color:var(--white)}
.btn-white{left:32px;top:385px;width:259px;height:42px;border-radius:21px;background:var(--white);color:var(--green);font-weight:700;font-size:20px;display:flex;align-items:center;justify-content:center}
.hero .opening{right:232px;top:592px;font-size:22px;line-height:33px;font-weight:600;color:var(--white);text-align:right}
/* intro */
.intro{top:800px;height:720px;background:var(--paper)}
.h2{width:1200px;text-align:center;font-weight:700;font-size:49px;color:var(--green)}
.intro .copy{right:111px;top:230px;width:400px;text-align:right;font-size:17px;line-height:20px;color:var(--text)}
.intro .copy p{margin-bottom:20px}
.btn-dark{background:var(--green);color:var(--white);font-weight:700;border-radius:22px;display:flex;align-items:center;justify-content:center;letter-spacing:2px}
/* services */
.services{top:1520px;height:820px;background:var(--white)}
.card{width:202px;height:300px}
.card .pic{width:202px;height:236px;border-radius:101px 101px 0 0;box-shadow:3px 3px 6px rgba(0,0,0,.25)}
.card .label{position:absolute;left:18px;top:194px;width:165px;height:100px;background:var(--white);box-shadow:2px 3px 6px rgba(0,0,0,.2);text-align:center;color:#444}
.card .label .t{height:62px;display:flex;align-items:center;justify-content:center;font-size:15.5px;line-height:17px;font-weight:500;padding:0 6px}
.card .label .m{display:inline-block;font-size:10px;font-weight:700;color:var(--green);padding:2px 8px;border-radius:8px;box-shadow:0 2px 3px rgba(0,0,0,.25)}
/* about */
.about{top:2340px;height:640px;background:var(--light)}
.about h2{left:508px;top:55px;font-size:50px;font-weight:700;color:var(--green)}
.about .copy{left:512px;top:146px;width:560px;font-size:15px;line-height:27px;font-weight:600;color:var(--green)}
.about .copy p{margin-bottom:4px}
.portrait{left:111px;top:148px;width:326px;height:326px;border-radius:50%;border:6px solid var(--white);background:radial-gradient(circle at 50% 40%,#e3b9a0 0 30%,#eaeaea 31%)}
/* contact */
.contact{top:2980px;height:740px;background:var(--white)}
.form{left:148px;top:193px;width:497px;height:420px;background:var(--green)}
.field{position:absolute;border:2px solid var(--white);border-radius:20px;color:var(--white);font-size:15px;font-weight:500;padding:9px 22px}
.btn-send{left:155px;top:316px;width:184px;height:40px;border-radius:20px;background:var(--white);color:var(--green);font-weight:700;font-size:15px;letter-spacing:1px;display:flex;align-items:center;justify-content:center}
.hours{left:656px;top:195px}
.hours h3{font-size:36px;font-weight:700;color:var(--green);margin-bottom:20px}
.hours p{font-size:15px;font-weight:700;color:var(--green);line-height:16px;margin-bottom:22.7px;letter-spacing:.3px}
/* newsletter */
.newsletter{top:3720px;height:455px;background:var(--paper)}
.newsletter .sub{width:1200px;top:200px;text-align:center;font-size:22px;line-height:27px;font-weight:600;color:#7a7a7a}
.email{left:311px;top:306px;width:401px;height:44px;background:var(--light);color:var(--white);font-size:14px;font-weight:600;padding:13px 18px}
/* footer */
.site-footer{top:4175px;height:163px;background:var(--green);color:var(--white)}
.site-footer .info{left:364px;top:48px;font-size:14px;line-height:20px;font-weight:700;letter-spacing:.5px}
.site-footer .copy{right:109px;top:98px;font-size:14px;font-weight:700;letter-spacing:.5px}
</style>
</head>
<body>

<header class="site-header">
  <div class="brand abs" style="left:128px;top:36px"><span class="dot"></span><span class="big">Dermatologie</span><span class="small">am Lindenhof</span></div>
  <nav class="nav">
    <a class="active" style="left:389px">Start</a>
    <a style="left:446px">Über Uns</a>
    <a style="left:537px">Leistungsspektrum</a>
    <a style="left:715px">Kontakt</a>
    <a style="left:796px">Termin online</a>
    <a style="left:934px">Für Zuweiser</a>
    <svg class="abs" style="left:1076px;top:48px" width="18" height="14" viewBox="0 0 18 14"><circle cx="6" cy="4" r="3" fill="#395722"/><path d="M0 13c0-4 3-5 6-5s6 1 6 5z" fill="#395722"/><circle cx="12" cy="4" r="2.6" fill="#395722"/><path d="M11 8c3 0 7 1 7 5h-5z" fill="#395722"/></svg>
  </nav>
</header>

<section class="hero">
  <svg class="abs" style="left:244px;top:474px" width="336" height="170"><path d="M0 0 A168 168 0 0 0 336 0 Z" fill="#ABCF8A"/></svg>
  <div class="abs" style="left:428px;top:69px;width:343px;height:491px;border-radius:172px 172px 0 0;border:6px solid var(--light);border-left:none;border-bottom:none"></div>
  <div class="abs" role="img" aria-label="Visualisierung Wohnquartier mit Baum und Grünfläche" style="left:416px;top:67px;width:355px;height:493px;background:linear-gradient(180deg,#dfe4e3 0%,#c9ccc0 45%,#8fa06f 80%,#b8b39a 100%);border-radius:172px 172px 0 0"></div>
  <div class="abs" style="left:823px;top:69px;width:343px;height:491px;border-radius:172px 172px 0 0;border:6px solid var(--light);border-left:none;border-bottom:none"></div>
  <div class="abs" role="img" aria-label="Visualisierung Neubau mit Radfahrerin" style="left:811px;top:67px;width:355px;height:493px;background:linear-gradient(180deg,#eef0f0 0%,#d5d1c2 50%,#9bab7c 85%,#c2c0b0 100%);border-radius:172px 172px 0 0"></div>
  <h1 class="abs">Dermatologie<br>am Lindenhof</h1>
  <p class="abs lead">Herzlich willkommen in der<br>Hautarztpraxis<br>im Lindenmatt-Quartier Basel!</p>
  <div class="abs btn-white">Termin vereinbaren</div>
  <p class="abs opening">Praxiseröffnung im Januar 2025!<br>Nähere Informationen folgen.</p>
</section>

<section class="intro">
  <h2 class="abs h2" style="top:100px">Wir sind für Sie da!</h2>
  <svg class="abs" style="left:0;top:0" width="700" height="720"><path d="M135 290 A113 113 0 0 1 345 210 Z" fill="#ABCF8A"/></svg>
  <div class="abs" role="img" aria-label="Frau mit geschlossenen Augen, Hautpflege" style="left:190px;top:230px;width:312px;height:337px;border-radius:156px 156px 0 0;background:linear-gradient(135deg,#f7e3df 0%,#efc9c0 55%,#f5dcd6 100%)"></div>
  <svg class="abs" style="left:0;top:0" width="700" height="720"><path d="M565 459 A110 110 0 0 1 358 530 Z" fill="#395722"/></svg>
  <div class="abs copy">
    <p>Dermatologie am Lindenhof ist eine moderne Praxis für allgemeine und ästhetische Dermatologie. Wir behandeln und beraten Sie bei allen Hauterkrankungen, Hautkrebs und Allergien.</p>
    <p>Wenn es darum geht, sich einfach wieder gut und schön zu fühlen in Ihrer Haut profitieren Sie von unserer Expertise in Lasermedizin und Soft-Ästhetik.</p>
    <p>Wir sind jederzeit gerne für Sie da! Kontaktieren Sie uns, um Ihre individuellen</p>
  </div>
  <div class="abs btn-dark" style="left:927px;top:521px;width:162px;height:42px;font-size:13px">KONTAKTIEREN</div>
</section>

<section class="services">
  <h2 class="abs h2" style="top:30px">Leistungsspektrum</h2>
  <div class="abs card" style="left:163px;top:143px"><div class="pic" role="img" aria-label="Hautuntersuchung mit Dermatoskop" style="background:linear-gradient(160deg,#e8c3aa,#b98a70)"></div><div class="label"><div class="t">Allgemeine Dermatologie</div><span class="m">mehr erfahren -&gt;</span></div></div>
  <div class="abs card" style="left:495px;top:143px"><div class="pic" role="img" aria-label="Chirurgische Instrumente" style="background:linear-gradient(160deg,#6d8fb8,#d6dde6)"></div><div class="label"><div class="t">Dermatochirurgie</div><span class="m">mehr erfahren -&gt;</span></div></div>
  <div class="abs card" style="left:830px;top:143px"><div class="pic" role="img" aria-label="Lichttherapie-Kabine" style="background:linear-gradient(160deg,#2f8fe0,#9fd3f7)"></div><div class="label"><div class="t">Lichttherapie</div><span class="m">mehr erfahren -&gt;</span></div></div>
  <div class="abs card" style="left:163px;top:474px"><div class="pic" role="img" aria-label="Pusteblumen vor blauem Himmel" style="background:linear-gradient(180deg,#6fb0e6,#dbe9f2 60%,#7aa34a)"></div><div class="label"><div class="t">Allergolie</div><span class="m">mehr erfahren -&gt;</span></div></div>
  <div class="abs card" style="left:495px;top:474px"><div class="pic" role="img" aria-label="Laserbehandlung" style="background:linear-gradient(160deg,#e6d2c6,#6d7f8e 60%,#3e6fb3)"></div><div class="label"><div class="t">Lasermedizin</div><span class="m">mehr erfahren -&gt;</span></div></div>
  <div class="abs card" style="left:830px;top:474px"><div class="pic" role="img" aria-label="Lachende Frau, Hautpflege" style="background:linear-gradient(160deg,#f4f1ee,#e0b8a0)"></div><div class="label"><div class="t">Soft-Ästhetik</div><span class="m">mehr erfahren -&gt;</span></div></div>
</section>

<section class="about">
  <svg class="abs" style="left:0;top:0" width="1200" height="640"><path d="M0 0 L388 0 C330 130 180 230 0 232 Z" fill="#395722"/><circle cx="1300" cy="1000" r="560" fill="#395722"/></svg>
  <div class="abs portrait" role="img" aria-label="Porträt des Praxisinhabers"></div>
  <h2 class="abs">Über uns</h2>
  <div class="abs copy">
    <p>Ich freue mich, dass Sie Ihr Weg auf die Seiten der “Dermatologie am Lindenhof” geführt hat!</p>
    <p>Es ist mir ein großes Anliegen, für Sie zu all Ihren Problemen an der Haut ein vertrauensvoller Ansprechpartner zu sein. Ich möchte Sie individuell als kompetenter Arzt sowie empathischer Mensch beraten und gemeinsam mit Ihnen die geeignete Therapie auswählen.</p>
    <p>Bei meiner Arbeit lege ich Wert auf eine wissenschaftlich aktuelle und leitliniengerechte Therapie, lasse aber immer Elemente<br>der alternativen Medizin einfliessen. Dies gehört für<br>mich zur integrativen Behandlung auf der<br>Grundlage eines ganzheitlichen<br>Menschenbildes.</p>
  </div>
  <div class="abs btn-dark" style="left:510px;top:533px;width:214px;height:42px;font-size:16px">mehr erfahren -&gt;</div>
</section>

<section class="contact">
  <h2 class="abs h2" style="top:48px">Kontakt</h2>
  <svg class="abs" style="left:100px;top:118px" width="600" height="520">
    <path d="M10 110 A98 98 0 0 1 205 70 Z" fill="#ABCF8A"/>
  </svg>
  <div class="abs form">
    <div class="field" style="left:40px;top:52px;width:198px">Vorname</div>
    <div class="field" style="left:255px;top:52px;width:198px">Nachname</div>
    <div class="field" style="left:40px;top:117px;width:198px">Email</div>
    <div class="field" style="left:255px;top:117px;width:198px">Telefonnummer</div>
    <div class="field" style="left:40px;top:182px;width:413px;height:116px">Nachricht</div>
    <div class="abs btn-send">ABSENDEN</div>
  </div>
  <svg class="abs" style="left:480px;top:520px" width="210" height="120"><path d="M202 5 A98 98 0 0 1 8 110 Z" fill="#ABCF8A"/></svg>
  <div class="abs hours">
    <h3>Öffnungszeiten</h3>
    <p>Montag: 08:30 – 12:00 &amp; 13:00 – 17:00</p>
    <p>Dienstag: 08:30 – 12:00 &amp; 13:00 – 17:00</p>
    <p>Mittwoch: 08:30 – 12:00 &amp; 14:30 – 18:00</p>
    <p>Donnerstag: 08:30 – 12:00, nachmittags geschlossen</p>
    <p>Freitag: 08:30 – 12:00, nachmittags geschlossen</p>
  </div>
</section>

<section class="newsletter">
  <h2 class="abs h2" style="top:110px">Newsletter abonnieren!</h2>
  <p class="abs sub">Bleiben Sie stets auf dem Laufenden<br>und melden Sie sich für unseren Newsletter an.</p>
  <div class="abs email">E-Mail</div>
  <div class="abs btn-dark" style="left:737px;top:306px;width:158px;height:44px;font-size:12px;letter-spacing:.5px">ABONNIEREN</div>
</section>

<footer class="site-footer">
  <div class="brand abs" style="left:148px;top:52px;color:var(--white)"><span class="dot"></span><span class="big" style="color:var(--white)">Dermatologie</span><span class="small" style="color:var(--white)">am Lindenhof</span></div>
  <div class="abs info">Straße 12,<br>12345 Irgendwo, Deutschland<br><span style="display:block;margin-top:6px">hallo@website.de</span></div>
  <div class="abs copy">© 2024 Dermatologie. Alle Rechte vorbehalten.</div>
</footer>

<svg class="abs" style="left:967px;top:715px" width="233" height="180"><path d="M0 85 A177 177 0 0 0 233 165 L233 0 Z" fill="#ABCF8A"/></svg>

</body>
</html>
```